Flyer for spiritual retreat (yoga, meditation, reiki, raw food)

I would like a flyer to promote my upcoming retreat and a matching Facebook banner.

The name of the retreat is "Wavecrest Of Calm" and the tagline is "retreat into you"

The activities in the retreat include daily meditation, ecstatic dance, spiritual development workshops on intuition, energy healing etc and a reiki session is included.

I would like a flyer designed to promote this, something that is editable as I will be running this multiple times and will need to adjust the flyer to add the dates etc each time.

edit: add that here will be fully catered raw food and juices, and that the retreat price includes all accomodation, meals and workshops.

Please contact me if you need further info. Please also visit my website www.marithovland.com and www.facebook.com/tolvanahaven to see my current events and promotions.

Thank you,

Marit

Reason: Hi all, thank you all for your submissions. Apologies as I am traveling and do not have much access to internet and will review your submissions and provide feedback as soon as possible. Kind regards, Marit.

Target Market(s)

People who like meditation, yoga, fans of rowan mabry and jasper vinek, those interested in personal and spiritual development.

Industry/Entity Type

Health And Wellness

Requirements
Must have
• Please put the included reiki session as as added bonus. Something like "BONUS 30 minute reiki healing session" in a little star/banner/something that stands out.
• Please emphasise the "light" part of Wavecrest as I am going for a play on words between in the light and enlightenment.
• Please include placeholder text for place, location, time
• Placeholder for price
• My name (see attached file - can change colour to suit) and website (www.marithovland.com)
Nice to have
• I prefer rounded designs, curves rather than block designs.
Should not have
• Tolvana Haven logo

```html
<!DOCTYPE html>
<html lang="en">
<head>
<meta charset="utf-8">
<title>Wavecrest Of Calm – Retreat Into You</title>
<link rel="stylesheet" href="https://fonts.googleapis.com/css2?family=Cinzel:wght@400&family=Great+Vibes&family=Kaushan+Script&family=Open+Sans:wght@400;700&family=Oswald:wght@500&display=swap">
<style>
  :root {
    --orange: #f2683a;
    --ink: #1f2a36;
    --heading: #22303f;
    --lilac: #c7b4e6;
    --peach: #f6d6c6;
    --teal: #5fcfc4;
    --badge-blue: #1f8fcf;
    --white: #ffffff;
  }
  * { margin: 0; padding: 0; box-sizing: border-box; }
  html, body { width: 927px; height: 1200px; overflow: hidden; background: var(--white); }
  .flyer {
    position: relative;
    width: 927px;
    height: 1200px;
    overflow: hidden;
  }
  .watercolour-wash {
    position: absolute; inset: 0;
    background:
      radial-gradient(ellipse 55% 35% at 15% 8%, var(--peach) 0%, transparent 70%),
      radial-gradient(ellipse 50% 40% at 85% 12%, var(--lilac) 0%, transparent 75%),
      radial-gradient(ellipse 60% 40% at 20% 60%, #d9c6ee 0%, transparent 75%),
      radial-gradient(ellipse 55% 35% at 80% 85%, var(--teal) 0%, transparent 70%),
      radial-gradient(ellipse 60% 40% at 25% 95%, #9fbdf0 0%, transparent 75%),
      linear-gradient(160deg, #f3e6f0 0%, #dce8f7 45%, #cfe6f4 70%, #c9ecea 100%);
  }
  .lotus-illustration {
    position: absolute;
    left: 0; top: 0;
    width: 590px; height: 360px;
    border-radius: 0 0 60% 45% / 0 0 55% 50%;
    background:
      radial-gradient(ellipse 18% 30% at 38% 45%, #eef3d8 0%, #eef3d8 55%, transparent 60%),
      radial-gradient(ellipse 60% 70% at 40% 40%, #2f7fc9 0%, #4fa3dc 45%, rgba(120,180,230,0.4) 75%, transparent 100%);
    opacity: 0.9;
  }
  .retreat-title {
    position: absolute;
    left: 40px; top: 340px;
    width: 860px;
    font-family: "Kaushan Script", cursive;
    font-size: 104px;
    line-height: 1;
    color: var(--orange);
    text-align: center;
    white-space: nowrap;
  }
  .retreat-title .light { font-size: 112px; }
  .intro {
    position: absolute;
    left: 397px; top: 502px;
    width: 408px;
  }
  .intro-heading {
    font-family: "Cinzel", serif;
    font-size: 35px;
    font-weight: 400;
    color: var(--heading);
    letter-spacing: 1px;
    line-height: 1.1;
    margin-bottom: 10px;
    white-space: nowrap;
  }
  .intro-body {
    font-family: "Open Sans", Verdana, sans-serif;
    font-size: 16.6px;
    line-height: 22.4px;
    letter-spacing: 0.7px;
    color: var(--ink);
    text-align: justify;
    hyphens: auto;
  }
  .intro-body .website { font-weight: 700; }
  .signature {
    position: absolute;
    left: 397px; top: 925px;
    width: 258px;
    font-family: "Great Vibes", cursive;
    font-size: 38px;
    line-height: 1.2;
    color: var(--heading);
    white-space: nowrap;
  }
  .reiki-badge {
    position: absolute;
    left: 662px; top: 901px;
    width: 182px; height: 182px;
  }
  .reiki-badge svg { display: block; }
  .reiki-badge .badge-text {
    position: absolute; inset: 0;
    display: flex; flex-direction: column; align-items: center; justify-content: center;
    text-align: center;
  }
  .badge-line {
    font-family: "Oswald", sans-serif;
    font-weight: 500;
    color: var(--white);
    font-size: 20px;
    line-height: 1;
  }
  .badge-reiki {
    font-family: "Kaushan Script", cursive;
    color: var(--orange);
    font-size: 48px;
    line-height: 0.95;
    margin: 2px 0 4px;
  }
  .details-bar {
    position: absolute;
    left: 0; top: 1116px;
    width: 927px;
    text-align: center;
    font-family: "Cinzel", serif;
    font-size: 30px;
    color: var(--orange);
    letter-spacing: 1px;
    white-space: nowrap;
  }
  .details-bar .divider { margin: 0 12px; }
</style>
</head>
<body>
<main class="flyer">
  <div class="watercolour-wash" role="img" aria-label="Soft watercolour background in peach, lilac, sky blue and teal with faint mandala patterns"></div>
  <div class="lotus-illustration" role="img" aria-label="Blue lotus flower with a pale silhouette of a person seated in meditation"></div>

  <h1 class="retreat-title">Wave<span class="light">crest</span> Of Calm</h1>

  <section class="intro">
    <h2 class="intro-heading">RETREAT INTO YOU</h2>
    <p class="intro-body">A transformational event that will teach you modern day techniques and method&shy;ologies for aligning your mind, body and soul to your true essence. We will combine this with the power of raw food. We will be in a group setting getting hands-on with our fully catered raw food as we begin to awaken our connection to the world around us. Retreat price includes all accomodation, meals and workshops with a bonus 30 minute reiki healing session. For more information: <span class="website">www.marithovland.com</span></p>
  </section>

  <p class="signature">— Marit Hovland</p>

  <div class="reiki-badge">
    <svg width="182" height="182" viewBox="0 0 190 190" aria-hidden="true">
      <circle cx="95" cy="95" r="93" fill="#ffffff"/>
      <circle cx="95" cy="95" r="83" fill="#1f8fcf"/>
      <circle cx="95" cy="95" r="77" fill="none" stroke="#ffffff" stroke-width="2"/>
    </svg>
    <div class="badge-text">
      <span class="badge-line">BONUS 30 MINS.</span>
      <span class="badge-reiki">Reiki</span>
      <span class="badge-line">SESSION</span>
    </div>
  </div>

  <p class="details-bar">Pricing<span class="divider">|</span>venue information<span class="divider">|</span>Date<span class="divider">|</span>Timings</p>
</main>
</body>
</html>
```